Brush up bramtide landing page projects.

Hello, we are organizing the bram-tide website.

http://www.bram-tide.jp

We are looking for a designer and need to brush up this landing page.
You don't need to worry about Japanese. Feel free to design the site in English.

http://www.bram-tide.jp/lp_c.html

please contact me.
Thank you.

```html
<!DOCTYPE html>
<html lang="en">
<head>
<meta charset="utf-8">
<title>Bramtide</title>
<link href="https://fonts.googleapis.com/css2?family=PT+Sans:wght@400;700&family=Arimo:wght@400;700&family=Oswald:wght@500&display=swap" rel="stylesheet">
<style>
:root{
  --teal:#129c9d;
  --teal-dark:#0d8586;
  --nav-active:#227476;
  --sky:#38c2ea;
  --pink:#e53a8b;
  --ink:#333;
  --body:#444;
  --link:#1d7897;
  --panel:#f5f5f5;
  --line:#e2e2e2;
}
*{box-sizing:border-box;margin:0;padding:0}
html,body{width:847px;height:1200px;overflow:hidden;background:#fff}
body{position:relative;font-family:"Arimo",Arial,sans-serif;color:var(--body)}
.abs{position:absolute}
h2,h3,h4{font-family:"PT Sans",sans-serif;font-weight:400;color:var(--ink)}

.site-header{left:0;top:0;width:847px;height:57px;background:var(--teal)}
.brand{left:92px;top:14px;color:#fff;font-family:"PT Sans",sans-serif;font-weight:700;font-size:22px;letter-spacing:.5px}
.nav{left:0;top:34px;width:847px;height:19px;font-size:8.6px;color:#fff}
.nav span{position:absolute;top:0;height:19px;line-height:19px}
.nav .active{background:var(--nav-active);padding:0 7px}

.slider{left:90px;top:77px;width:666px;height:277px;border-radius:12px;background:#f0f0f0;border:1px solid #e4e4e4;box-shadow:0 2px 4px rgba(0,0,0,.08)}
.slider-inner{left:20px;top:18px;width:628px;height:241px;border-radius:8px;background:#fff}
.slide{left:7px;top:7px;width:613px;height:226px;border-radius:3px;background:linear-gradient(90deg,#e8efdc 0%,#c9dca8 45%,#b5cf8a 100%)}
.arrow{width:35px;height:30px;border-radius:0 8px 8px 0;background:#2b2b2b;top:127px}
.arrow.prev{left:9px}
.arrow.next{left:622px;border-radius:8px 0 0 8px}
.dots{left:296px;top:245px;width:76px;height:20px;border-radius:10px;background:#f4f4f4;border:1px solid #d8d8d8;display:flex;justify-content:center;align-items:center;gap:3px}
.dots i{width:8px;height:8px;border-radius:50%;background:#555}
.dots i:first-child{background:#fff;border:1.5px solid #666}

.intro-title{left:94px;top:384px;font-size:18px;font-weight:700}
.intro-photo{left:94px;top:419px;width:211px;height:103px;background:linear-gradient(135deg,#c8d43a,#3b6fb5 60%,#e2e6ea)}
.intro-text{left:314px;top:418px;width:452px;font-size:8.8px;line-height:14px}
.intro-text p+p{margin-top:7px}

.services{left:86px;top:553px;width:495px;height:274px;background:var(--panel);border:1px solid var(--line)}
.services h2{position:absolute;left:9px;top:8px;font-size:16.5px}
.card{position:absolute;top:40px;width:140px}
.card .thumb{width:122px;height:92px;border:3px solid #ddd}
.card h3{font-size:13.5px;font-weight:700;margin-top:11px;white-space:nowrap}
.card p{font-size:8.2px;line-height:12.8px;margin-top:5px}
.divider{position:absolute;top:40px;width:1px;height:222px;background:var(--line)}

.live{left:590px;top:554px;width:184px;height:265px;background:var(--sky)}
.live h4{position:absolute;left:12px;top:6px;color:#fff;font-weight:700;font-size:13px}
.live-body{position:absolute;left:4px;top:32px;width:177px;height:200px;background:#fff;padding:0 10px}
.tweet{font-size:7.6px;line-height:12.2px;color:#555;padding:10px 0 8px;border-bottom:1px solid #eee}
.tweet:last-child{border:0}
.tweet .ago{color:var(--sky);display:block}
.live .label{position:absolute;left:12px;top:242px;color:#fff;font-family:"PT Sans",sans-serif;font-weight:700;font-size:13px}

.news{left:84px;top:852px;width:495px;height:174px;background:var(--panel);border:1px solid var(--line)}
.news h2{position:absolute;left:9px;top:5px;font-size:16.5px}
.item{position:absolute;left:7px;width:470px}
.avatar{position:absolute;left:0;top:0;width:35px;height:34px;background:#ececec;border:1px solid #ddd}
.item h3{position:absolute;left:40px;top:-6px;font-size:13px;font-weight:700;color:var(--link);letter-spacing:.3px;white-space:nowrap}
.item .date{position:absolute;left:42px;top:12px;font-size:6.8px;color:#666}
.item p{position:absolute;left:42px;top:21px;width:420px;font-size:7.8px;line-height:10px;color:#555}
.news hr{position:absolute;left:7px;top:103px;width:457px;border:0;border-top:1px solid #ddd}

.ad{left:590px;top:837px;width:176px;height:188px;background:var(--teal);border-radius:2px}
.ad h4{position:absolute;left:0;top:6px;width:176px;text-align:center;font-family:"Oswald",sans-serif;font-weight:500;color:#fff;font-size:16px;letter-spacing:.5px}
.ad-photo{position:absolute;left:3px;top:39px;width:170px;height:86px;background:linear-gradient(90deg,#f1ece6,#fff)}
.bubble{position:absolute;left:66px;top:42px;width:100px;height:36px;background:#f4f4f4;border:1px solid #ccc;border-radius:4px;font-family:"PT Sans",sans-serif;font-size:9.6px;line-height:12.5px;padding:4px 7px;color:#555}
.bubble b{color:var(--pink)}
.bubble span{color:var(--teal)}
.ad-cta{position:absolute;left:3px;top:125px;width:170px;height:60px;background:var(--pink);color:#fff;font-family:"PT Sans",sans-serif;font-size:13px;line-height:17px;text-align:center;padding-top:13px}

.site-footer{left:0;top:1034px;width:847px;height:144px;background:var(--teal)}
.fcol{position:absolute;top:12px;color:#fff}
.fcol h4{color:#fff;font-size:13px;font-weight:700;font-family:"PT Sans",sans-serif;height:26px}
.fcol ul{list-style:none;font-size:9.4px;line-height:15.6px}
.fcol li::before{content:"›";color:#7fd0d0;margin-right:5px}
.copy-bar{left:0;top:1178px;width:847px;height:22px;background:var(--teal-dark);color:#fff;font-size:9.6px;text-align:center;line-height:22px}
.social{position:absolute;top:6px;width:11px;height:11px;border-radius:2px}
</style>
</head>
<body>

<header class="site-header abs">
  <div class="brand abs">bramtide</div>
  <nav class="nav abs">
    <span class="active" style="left:346px">Putting in order</span>
    <span style="left:447px">Custody</span>
    <span style="left:513px">Eco collection and acquisition</span>
    <span style="left:664px">Vendoru</span>
    <span style="left:727px">Thrift shop</span>
  </nav>
</header>

<section class="slider abs">
  <div class="slider-inner abs">
    <div class="slide abs" role="img" aria-label="Staff in branded jackets beside a child dropping a carton into a recycling bin"></div>
    <div class="dots abs"><i></i><i></i><i></i><i></i><i></i></div>
  </div>
  <svg class="arrow prev abs" viewBox="0 0 35 30"><path d="M14 9l7 6-7 6" fill="none" stroke="#fff" stroke-width="3"/></svg>
  <svg class="arrow next abs" viewBox="0 0 35 30"><path d="M21 9l-7 6 7 6" fill="none" stroke="#fff" stroke-width="3"/></svg>
</section>

<h2 class="intro-title abs">ECO Less is Beautiful.</h2>
<div class="intro-photo abs" role="img" aria-label="Workers sorting items on a factory line"></div>
<div class="intro-text abs">
  <p>The goal at tallyback is to create an environment for both poker players and poker rooms to prosper and grow the poker community as a whole. We are currently in the process of designing and creating features to help poker players. We highly value poker players' input poker players and poker rooms to prosper and grow the poker community as a whole. We are currently in poker players and poker rooms to prosper and grow the poker community as a whole.</p>
  <p>We are currently in poker players and poker rooms to prosper and grow the poker community as a whole. We are currently inand would greatly appreciate any feedback on issues or services that players would like to see offered.</p>
</div>

<section class="services abs">
  <h2>Recommended service of Bramtide</h2>
  <div class="card" style="left:6px">
    <div class="thumb" role="img" aria-label="Visitors touring an industrial plant" style="background:linear-gradient(180deg,#b9cbe0,#8a9aa8)"></div>
    <h3>Givewear</h3>
    <p>Please offer your precious clothes you. I had from our important "clothes" changes to working capital of summer camp for children.</p>
  </div>
  <div class="divider" style="left:154px"></div>
  <div class="card" style="left:180px">
    <div class="thumb" role="img" aria-label="Worker among heaps of plastic bottles" style="background:linear-gradient(135deg,#3f66b5,#8fa7d6 50%,#c94a4a)"></div>
    <h3>Eco-Marlow charity</h3>
    <p>Vendoru is a unique auction site that someone is not only exhibi-tion and "things that are no longer used". I want to know more and more people, this Vendoru.</p>
  </div>
  <div class="divider" style="left:323px"></div>
  <div class="card" style="left:343px">
    <div class="thumb" role="img" aria-label="Workers in hard hats at a machine" style="background:linear-gradient(135deg,#5a7a9c,#2d4f8a 55%,#d8c34a)"></div>
    <h3>Service putting in order</h3>
    <p>Will help the packing of moving and putting in order the room service your putting in order of Bramtide. I will not be refreshing a room of professional clean up makes a consulting firm.</p>
  </div>
</section>

<aside class="live abs">
  <h4>Live Updates</h4>
  <div class="live-body">
    <div class="tweet">Northgate Signals is continuing to dominate. Make sure you sign up soon if you want to follow this amazing trader. Subs cut off at 500!<span class="ago">10 days ago</span></div>
    <div class="tweet">Do you need a forex VPS? Check out our sister business! http://lnk.example/q7RmT2<span class="ago">27 days ago</span></div>
    <div class="tweet">Northgate Signals is above his watermark high with a 32 Pip winner yesterday!<span class="ago">56 days ago</span></div>
  </div>
  <div class="label">updates</div>
</aside>

<section class="news abs">
  <h2>Info New Arrival News &amp; profitable</h2>
  <div class="item" style="top:36px">
    <div class="avatar"></div>
    <h3>Eco festival be held (Sun) Bramtide the 20th [recycling]</h3>
    <div class="date">Posted October 17, 2012</div>
    <p>Please offer your precious clothes you. I had from our important "clothes" changes to working capital of summer camp for children.Please offer your precious clothes you. I had from our important "clothes" changes to working capital of summer camp for children.</p>
  </div>
  <hr>
  <div class="item" style="top:113px">
    <div class="avatar"></div>
    <h3>Campaign for putting in order [service]!</h3>
    <div class="date">Posted September 13, 2012 by</div>
    <p>Please offer your precious clothes you. I had from our important "clothes" changes to working capital of summer camp for children.</p>
  </div>
</section>

<aside class="ad abs">
  <h4>ADVERTISING SPACE</h4>
  <div class="ad-photo" role="img" aria-label="Woman smiling at her phone"></div>
  <div class="bubble">Nice little thing <b>♥</b><br><span>eco recovery</span></div>
  <div class="ad-cta">Simple request for ›<br>quotation</div>
</aside>

<footer class="site-footer abs">
  <div class="fcol" style="left:84px">
    <h4>Service of Bramtide</h4>
    <ul><li>Bramtide</li><li>Putting in order</li><li>Custody</li><li>Eco collection and purchase</li><li>Vendoru</li><li>Thrift shop</li></ul>
  </div>
  <div class="fcol" style="left:245px">
    <h4>I can also be like this</h4>
    <ul><li>Full access to buy household</li><li>Purchase of brand-name products</li><li>You bring in eco-products recovery</li><li>Date and time specified service</li><li>PC data erasure services</li></ul>
  </div>
  <div class="fcol" style="left:441px">
    <h4>Corporate information</h4>
    <ul><li>Corporate Profile</li><li>Management philosophy</li><li>Media information</li><li>Privacy Policy</li><li>Bram-Tide Partnership</li></ul>
  </div>
  <div class="fcol" style="left:625px">
    <h4>&nbsp;</h4>
    <ul><li>Corporate Profile</li><li>Management philosophy</li><li>Media information</li><li>Privacy Policy</li><li>Bram-Tide Partnership</li></ul>
  </div>
</footer>

<div class="copy-bar abs">
  Copyright© 2013 HALVERN STUDIO ALL RIGHT RESERVED.
  <span class="social" style="left:719px;background:#f08a24"></span>
  <span class="social" style="left:733px;background:#3b5998"></span>
  <span class="social" style="left:747px;background:#d34836"></span>
  <span class="social" style="left:761px;background:#3aa9e0"></span>
</div>

</body>
</html>
```